Corvell Climate Job Add

We need a flashy ad we can post around our marketplace to attract new talent and employee. Our website has our company theme https://corvellclimate.ca/

Target Market(s)

HVAC, Refrigeration, Trades

Industry/Entity Type

Trades

Requirements
Must have
• a few key phrases such as "Paying above industry standard" and "No on-call requirements"

```html
<!DOCTYPE html>
<html lang="en">
<head>
<meta charset="UTF-8">
<title>Corvell Climate – Now Hiring</title>
<link rel="stylesheet" href="https://fonts.googleapis.com/css2?family=Open+Sans:wght@700;800&family=Montserrat:wght@400;500&family=Roboto:wght@400;500&display=swap">
<style>
  :root {
    --orange: #f05a22;
    --blue: #0a72c8;
    --ink: #111111;
    --text: #222222;
    --paper: #f1f1f1;
    --white: #ffffff;
  }
  html, body {
    margin: 0;
    padding: 0;
    overflow: hidden;
    background: var(--white);
  }
  .ad {
    position: relative;
    width: 1200px;
    height: 849px;
    overflow: hidden;
    background: var(--paper);
    font-family: "Open Sans", Arial, sans-serif;
  }
  .ad__graphics {
    position: absolute;
    inset: 0;
    width: 1200px;
    height: 849px;
  }
  .ad__text {
    position: absolute;
    margin: 0;
    line-height: 1;
    white-space: nowrap;
  }
  .phones {
    left: 52px;
    top: 33px;
    font-size: 27px;
    font-weight: 800;
    color: var(--ink);
    line-height: 29px;
  }
  .headline {
    left: 418px;
    font-size: 59px;
    font-weight: 800;
    letter-spacing: -0.3px;
  }
  .headline--top { top: 72px; color: var(--orange); }
  .headline--bottom { top: 125px; color: var(--ink); }
  .perk {
    left: 459px;
    top: 201px;
    font-size: 42px;
    font-weight: 700;
    color: var(--blue);
  }
  .service {
    left: 609px;
    font-size: 46px;
    font-weight: 800;
    letter-spacing: -0.2px;
  }
  .service--lead { top: 356px; color: var(--ink); }
  .service--accent { top: 398px; color: var(--orange); }
  .service--tail { top: 440px; color: var(--ink); }
  .region {
    left: 608px;
    top: 516px;
    font-family: "Montserrat", Arial, sans-serif;
    font-weight: 400;
    font-size: 31px;
    letter-spacing: 0.4px;
    color: var(--blue);
  }
  .blurb {
    left: 610px;
    top: 556px;
    font-family: "Roboto", Arial, sans-serif;
    font-size: 13.5px;
    line-height: 17px;
    color: var(--text);
    white-space: normal;
    width: 340px;
  }
  .brand {
    position: absolute;
    left: 880px;
    top: 640px;
    width: 270px;
    display: flex;
    flex-direction: column;
    align-items: center;
    gap: 12px;
  }
  .brand__dot {
    width: 86px;
    height: 86px;
    border-radius: 50%;
    background: var(--orange);
  }
  .brand__name {
    font-family: "Open Sans", Arial, sans-serif;
    font-weight: 800;
    font-size: 30px;
    color: var(--blue);
    white-space: nowrap;
    line-height: 1;
  }
</style>
</head>
<body>
<main class="ad">
  <svg class="ad__graphics" viewBox="0 0 1200 849" xmlns="http://www.w3.org/2000/svg">
    <defs>
      <linearGradient id="plantTone" x1="0" y1="0" x2="1" y2="1">
        <stop offset="0" stop-color="#f4f4f4"/>
        <stop offset="0.5" stop-color="#e6e6e6"/>
        <stop offset="1" stop-color="#efefef"/>
      </linearGradient>
      <linearGradient id="workerTone" x1="0" y1="0" x2="1" y2="1">
        <stop offset="0" stop-color="#4a4c50"/>
        <stop offset="0.45" stop-color="#2c2e33"/>
        <stop offset="0.8" stop-color="#6d7076"/>
        <stop offset="1" stop-color="#9a9ca0"/>
      </linearGradient>
    </defs>

    <rect class="backdrop" role="img" aria-label="Faded industrial plant room with pipes and pumps" width="1200" height="849" fill="url(#plantTone)"/>

    <polygon class="band band--orange" points="0,65 300,240 560,620 785,849 220,849 0,665" fill="var(--orange)"/>
    <polygon class="corner corner--blue" points="975,0 1200,0 1200,225" fill="var(--blue)"/>

    <line class="stripe stripe--orange" x1="63" y1="-4" x2="300" y2="228" stroke="var(--orange)" stroke-width="9" stroke-linecap="round"/>
    <line class="stripe stripe--blue" x1="107" y1="-4" x2="355" y2="238" stroke="var(--blue)" stroke-width="11" stroke-linecap="round"/>

    <circle class="perk-dot" cx="430" cy="224" r="15" fill="var(--orange)"/>

    <polygon class="hex-plate" points="113,690 113,711 312,823 512,711 512,690" fill="var(--white)"/>
    <polygon class="hex-frame" points="312,234 559,376 559,653 312,800 65,661 65,376" fill="var(--blue)"/>
    <polygon class="hex-gap" points="312,245 550,382 550,650 312,788 75,654 75,382" fill="var(--white)"/>
    <polygon class="hex-photo" role="img" aria-label="Technician in an orange hard hat and safety glasses working on mechanical equipment" points="312,253 543,387 543,651 312,781 84,651 84,387" fill="url(#workerTone)"/>
  </svg>

  <p class="ad__text phones">(403) 555-0148<br>(780) 555-0172</p>

  <h1 class="ad__text headline headline--top">PAYING ABOVE</h1>
  <p class="ad__text headline headline--bottom">INDUSTRY STANDARD</p>

  <p class="ad__text perk">No on-call requirements</p>

  <h2 class="ad__text service service--lead">AFFORDABLE</h2>
  <p class="ad__text service service--accent">MECHANICAL SYSTEM</p>
  <p class="ad__text service service--tail">MAINTENANCE</p>

  <p class="ad__text region">CALGARY + EDMONTON</p>
  <p class="ad__text blurb">We offer full-service solutions for commercial and condo buildings in Calgary and Edmonton</p>

  <div class="brand">
    <span class="brand__dot"></span>
    <span class="brand__name">Corvell Climate Inc</span>
  </div>
</main>
</body>
</html>
```